Flyer for New Spa Opening

We need a flyer to increase customer's awareness of our new spa located in Yangon, Myanmar, in a middle-upper class shopping mall. A new hotel will be opening above the mall in Dec 2013.
Updates

Have made payment guaranteed.  Need a good flyer. Thanks.

Hi, I have uploaded a Words File for Flyer Text. Thanks!

Dear Designers,

I have setup a 2nd award, there's too many outstanding designs! Thanks so much.

Regards
Marla

Target Market(s)

-Hotel guest who wants to a spa session to relax
-Woman between 18 - 55 years old who have high spending power in a poor country(Myanmar). They like to use "Big Brands" but do not have much variety available in their country.

Industry/Entity Type

Shopping

Requirements
Must have
• Our services include Body Spa, Facial, Nails, Waxing & Foot Reflexology. We use well-known international brands in our spa including Veridelle, KRU, Varnet, Brisola Terrano and MORLU.

Veridelle, the skin care system researched and developed by The Halvern Dermal Academy (HDA), is an international leader in today’s skin care industry.

We are authorized Veridelle skin spa to provide professional facial and retailing Veridelle products.

Include the logo of the brands

Willowmere Spa
add: No 72, Thuka Road, Min Ye Plaza (Level-5) (6187), Kyimyin Township, Yangon
tel: +959 47208613
email: contactus@velmora-unitedgroup.example

Nice to have
• visually nice and relaxing spa pictures.
Should not have
• price

```html
<!DOCTYPE html>
<html lang="en">
<head>
<meta charset="utf-8">
<title>Willowmere Spa Flyer</title>
<link rel="stylesheet" href="https://fonts.googleapis.com/css2?family=Roboto+Condensed:wght@400;700&family=Open+Sans:ital,wght@0,400;0,600;0,700;1,400&display=swap">
<style>
:root{
  --bg:#e9e6e1;
  --blue:#1a6fba;
  --blue-dark:#0f5aa0;
  --green:#8cc63f;
  --green-light:#c9e27a;
  --green-dark:#5a9a1c;
  --ink:#3a3a3a;
  --ink-soft:#555;
  --dark:#1f2a14;
  --red:#e0314b;
  --white:#fff;
  --tile:#f4f4f4;
}
*{box-sizing:border-box;margin:0;padding:0}
html,body{width:1200px;height:900px;overflow:hidden;background:var(--bg)}
body{position:relative;font-family:"Open Sans",Arial,sans-serif;color:var(--ink)}
.page{position:absolute;top:113px;width:505px;height:714px;background:var(--white);overflow:hidden;box-shadow:0 2px 8px rgba(0,0,0,.25)}
.page--back{left:88px}
.page--front{left:615px}
.swoosh{position:absolute;left:0;width:505px;z-index:0}

/* back */
.tab{position:absolute;z-index:1;height:25px;background:var(--blue);color:var(--white);font:700 15px/25px "Roboto Condensed",Arial,sans-serif;padding-left:30px;border-radius:0 13px 13px 0}
.tab--right{border-radius:13px}
.col{position:absolute;z-index:1;font-size:7.6px;line-height:10.2px;color:var(--ink-soft)}
.col p{margin-bottom:8px;text-align:justify}
.col b{color:var(--ink)}
.treat{font:700 10.5px/14px "Roboto Condensed",Arial,sans-serif;color:var(--blue);margin:4px 0 4px}
.treat--rule{border-bottom:1px solid #9aa;padding-bottom:2px;margin:0}
.incl{font-style:italic;font-size:6.4px;color:#666}
.badge-oval{position:absolute;z-index:2;left:45px;top:450px;width:200px;height:155px;border-radius:50%;background:var(--blue);border:3px solid var(--white);box-shadow:0 0 0 2px var(--blue);color:var(--white);text-align:center;font:700 10.5px/13px "Roboto Condensed",Arial,sans-serif;padding:20px 18px 0}
.badge-oval p+p{margin-top:6px}
.hands-photo{position:absolute;z-index:2;left:292px;top:535px;width:182px;height:170px;border-radius:50%;border:4px solid var(--white);background:radial-gradient(circle at 50% 45%,#f6c9a9,#e7a37b 60%,#d9875f)}
.address{position:absolute;z-index:2;left:36px;top:618px;font:700 9.6px/13px "Roboto Condensed",Arial,sans-serif;color:var(--dark)}
.call{position:absolute;z-index:2;left:36px;font:700 20px/1 "Roboto Condensed",Arial,sans-serif;color:var(--white)}
.call small{font-size:15px}
.email{position:absolute;z-index:2;left:36px;font:700 12px/1 "Roboto Condensed",Arial,sans-serif;color:var(--white)}

/* front */
.title{position:absolute;left:54px;top:22px;font:700 40px/1 "Roboto Condensed",Arial,sans-serif;color:var(--white);letter-spacing:.5px;text-shadow:0 1px 2px rgba(0,0,0,.2)}
.hero-photo{position:absolute;left:250px;top:0;width:255px;height:370px;background:radial-gradient(ellipse at 55% 45%,#f0d3bd 0%,#e6bfa3 35%,rgba(255,255,255,0) 70%)}
.brand{position:absolute;border:1px solid #999;border-radius:3px;background:var(--tile);color:#555;font:700 11px/1 "Roboto Condensed",Arial,sans-serif;display:flex;align-items:center;justify-content:center;text-align:center}
.brand--main{left:30px;top:180px;width:143px;height:28px;font-size:17px}
.services-title{position:absolute;left:25px;top:264px;font:700 24px/1 "Roboto Condensed",Arial,sans-serif;color:var(--blue)}
.service{position:absolute;left:46px;font:700 16px/1 "Roboto Condensed",Arial,sans-serif;color:#333}
.service::before{content:"";position:absolute;left:-22px;top:3px;width:12px;height:12px;border-radius:50%;background:radial-gradient(circle at 35% 35%,#f7a0a8,var(--red) 60%)}
.sub{position:absolute;left:48px;top:373px;list-style:none;font:600 8.4px/14px "Open Sans",Arial,sans-serif;color:#333}
.sub li{padding-left:16px;position:relative}
.sub svg{position:absolute;left:0;top:3px}
.photo{position:absolute;left:310px;width:180px;height:102px;border:2px solid var(--white);border-radius:6px;box-shadow:0 1px 3px rgba(0,0,0,.2)}
.products-photo{position:absolute;left:8px;top:485px;width:302px;height:125px;background:linear-gradient(90deg,#e9d2c2 0%,#f1e1d8 35%,#d9a0a8 60%,#efd6cf 100%);border-radius:4px}
.front-call{position:absolute;left:25px;top:616px;font:700 29px/1 "Roboto Condensed",Arial,sans-serif;color:var(--dark)}
.front-email{position:absolute;left:25px;top:657px;font:700 13.5px/1 "Roboto Condensed",Arial,sans-serif;color:var(--dark)}
.brands-note{position:absolute;left:10px;top:684px;width:465px;height:20px;background:var(--red);border-radius:10px;color:var(--white);font:600 7.6px/20px "Open Sans",Arial,sans-serif;text-align:center}
</style>
</head>
<body>

<section class="page page--back">
  <svg class="swoosh" style="top:420px" width="505" height="294" viewBox="0 0 505 294" aria-hidden="true">
    <defs>
      <linearGradient id="backGreen" x1="0" y1="0" x2="0" y2="1">
        <stop offset="0" stop-color="#b9dc5a"/><stop offset="1" stop-color="#7dbb2e"/>
      </linearGradient>
    </defs>
    <path d="M0 12 C150 -8 330 60 505 112 L505 294 L0 294 Z" fill="url(#backGreen)"/>
    <path d="M0 12 C150 -8 330 60 505 112" fill="none" stroke="#fff" stroke-width="3"/>
    <path d="M0 34 C160 20 330 90 505 136" fill="none" stroke="#e4f2b0" stroke-width="6" opacity=".7"/>
  </svg>

  <div class="tab" style="left:0;top:27px;width:138px">Facial</div>
  <div class="tab tab--right" style="left:246px;top:27px;width:231px;padding-left:16px">Body Spa</div>

  <div class="col" style="left:30px;top:66px;width:213px">
    <p>We are authorized Veridelle skin spa to provide Professional Facial and Retailing Veridelle products.</p>
    <p>Veridelle, the skin care system from US, researched and developed by The Halvern Dermal Academy (HDA), is an international leader in today's skin care industry.</p>
    <p>Chose from a <b>Customized Facial</b> or <b>Targeted Treatment Facial</b></p>
    <p>Customized Facial is designed to address every client's skin type and concern. Our professionally trained therapists will careful select the product and procedure that is most suitable for your skin to achieve true skin health.</p>
    <p><b>Targeted Treatment</b> includes <b>LumaBrightRX Facial, TimeRenew Facial, SoftCalm Facial</b> and <b>PureClear Facial</b>. Tell us your skin concern and we have the solution just for you!</p>
  </div>

  <div class="tab" style="left:0;top:277px;width:138px">Nails</div>
  <div class="col" style="left:30px;top:310px;width:213px">
    <p>We know you love KRU! We have over 200 choices of KRU colours just for you. Our Nail Technicians are trained to provide the most meticulous Manicure &amp; Pedicure according to the <b>Professional System by KRU</b>.</p>
  </div>

  <div class="tab" style="left:0;top:372px;width:138px">Waxing</div>
  <div class="col" style="left:34px;top:408px;width:213px">
    <p>We take care of all the unsightly hairy body parts, just leave it to us. Walk out like a new sexy you!</p>
  </div>

  <div class="col" style="left:262px;top:66px;width:221px">
    <p>Indulge your body, mind and soul in one of our relaxing Spa Treatments.</p>
    <div class="treat">Willowmere Day Spa (2.5hr)</div>
    <p>A luxurious spa experience designed for total relaxation. A delightful body scrub will leave your skin smooth to the touch, followed by a 60min Swedish Aromatherapy massage. The treatment is complete with a body wrap to nourish your skin and your head gently massaged, giving you a profound sense of pleasure and well-being.</p>
    <p class="incl">Includes: Body Scrub - 60min Swedish Aromatherapy Massage - Body Wrap with Head Massage.</p>
    <div class="treat treat--rule">Traditional Body Massage (1.5hr)</div>
    <div class="treat treat--rule">Swedish Aromatherapy Body Massage (1.5hr)</div>
    <div class="treat">Revitalizing Body Scrub (1hr)</div>
    <p>Your skin is polished smooth and soft to the touch followed by a luxurious body cream massaged in to hydrate the newly revealed skin.</p>
    <p class="incl">Includes: Body Scrub - Light Body Massage</p>
    <div class="treat" style="font-size:12px">Pampering Body Treatment (1.5hr)</div>
    <p>An all over body treatment begins with a body scrub to exfoliate dead skin, in preparation for a body wrap that restores your skin to youthful condition. Lastly a luxurious body cream is massaged in leaving your skin beautifully radiant.</p>
    <p class="incl">Includes: Body Scrub - Body Wrap with Head Massage - Light Body Massage.</p>
    <div class="treat" style="font-size:12px">Foot Massage (1hr)</div>
    <p>Pamper your foot that has taken you a hundred miles. Following a foot soak and cleaning, we will begin foot massage on your foot reflex zones stimulating body energy and on your muscles to soothe tired heavy legs.</p>
    <p class="incl">Includes: Foot Soak - Foot Massage</p>
  </div>

  <div class="badge-oval">
    <p>Veridelle, the skin care system researched and developed by The Halvern Dermal Academy (HDA), is an international leader in today's skin care industry.</p>
    <p>We are authorized Veridelle skin spa to provide professional facial and retailing Veridelle products.</p>
  </div>
  <div class="hands-photo" role="img" aria-label="Photo of hands giving a relaxing hand massage"></div>

  <div class="address">No 72, Thuka Road, Min Ye Plaza<br>(Level-5) (6187), Kyimyin Township, Yangon</div>
  <div class="call" style="top:656px"><small>Call: </small>+959 47208613</div>
  <div class="email" style="top:686px">Email: contactus@velmora-unitedgroup.example</div>
</section>

<section class="page page--front">
  <svg class="swoosh" style="top:0" width="505" height="260" viewBox="0 0 505 260" aria-hidden="true">
    <defs>
      <linearGradient id="topGreen" x1="0" y1="0" x2="1" y2="1">
        <stop offset="0" stop-color="#6fb32a"/><stop offset=".6" stop-color="#a6d14a"/><stop offset="1" stop-color="#d8ec9a"/>
      </linearGradient>
    </defs>
    <path d="M0 0 H505 V120 C380 60 200 100 0 160 Z" fill="url(#topGreen)"/>
    <path d="M0 175 C180 110 360 70 505 135" fill="none" stroke="#c9e27a" stroke-width="10" opacity=".6"/>
    <path d="M0 160 C200 100 380 60 505 120" fill="none" stroke="#fff" stroke-width="3"/>
  </svg>

  <div class="hero-photo" role="img" aria-label="Photo of a woman wrapped in a white towel, seen from behind"></div>
  <h1 class="title">Willowmere Spa</h1>

  <div class="brand brand--main">Veridelle</div>
  <div class="brand" style="left:30px;top:213px;width:30px;height:32px;font-size:8px">MORLU</div>
  <div class="brand" style="left:63px;top:213px;width:54px;height:32px;font-size:8px">Brisola<br>Terrano</div>
  <div class="brand" style="left:120px;top:213px;width:54px;height:32px;font-size:10px">Varnet</div>
  <div class="brand" style="left:177px;top:213px;width:66px;height:32px;font-size:16px">KRU</div>

  <div class="services-title">OUR SERVICES</div>
  <div class="service" style="top:301px">Facial</div>
  <div class="service" style="top:325px">Nails</div>
  <div class="service" style="top:349px">Body Spa</div>
  <ul class="sub">
    <li><svg width="10" height="9" viewBox="0 0 10 9"><rect width="10" height="9" fill="#3c8d1e"/><path d="M2 4.5 L4.2 6.8 L8.3 1.8" stroke="#fff" stroke-width="1.6" fill="none"/></svg>Willowmere Day Spa (2.5hr)</li>
    <li><svg width="10" height="9" viewBox="0 0 10 9"><rect width="10" height="9" fill="#3c8d1e"/><path d="M2 4.5 L4.2 6.8 L8.3 1.8" stroke="#fff" stroke-width="1.6" fill="none"/></svg>Traditional Body Massage (1.5hr)</li>
    <li><svg width="10" height="9" viewBox="0 0 10 9"><rect width="10" height="9" fill="#3c8d1e"/><path d="M2 4.5 L4.2 6.8 L8.3 1.8" stroke="#fff" stroke-width="1.6" fill="none"/></svg>Swedish Aromatherapy Body Massage (1.5hr)</li>
    <li><svg width="10" height="9" viewBox="0 0 10 9"><rect width="10" height="9" fill="#3c8d1e"/><path d="M2 4.5 L4.2 6.8 L8.3 1.8" stroke="#fff" stroke-width="1.6" fill="none"/></svg>Revitalizing Body Scrub (1hr)</li>
    <li><svg width="10" height="9" viewBox="0 0 10 9"><rect width="10" height="9" fill="#3c8d1e"/><path d="M2 4.5 L4.2 6.8 L8.3 1.8" stroke="#fff" stroke-width="1.6" fill="none"/></svg>Pampering Body Treatment (1.5hr)</li>
    <li><svg width="10" height="9" viewBox="0 0 10 9"><rect width="10" height="9" fill="#3c8d1e"/><path d="M2 4.5 L4.2 6.8 L8.3 1.8" stroke="#fff" stroke-width="1.6" fill="none"/></svg>Foot Massage (1hr)</li>
  </ul>
  <div class="service" style="top:462px">Waxing</div>

  <div class="photo" style="top:357px;background:linear-gradient(135deg,#f3ece6,#e9d6c8 50%,#d6c2b2)" role="img" aria-label="Photo of a facial mask treatment"></div>
  <div class="photo" style="top:466px;background:linear-gradient(135deg,#f0dccd,#e3bfa4 50%,#c99c80)" role="img" aria-label="Photo of a relaxing back massage"></div>
  <div class="photo" style="top:576px;background:linear-gradient(135deg,#efe3d6,#dcc3ab 50%,#b99a7e)" role="img" aria-label="Photo of a hot stone massage"></div>

  <svg class="swoosh" style="top:560px" width="505" height="154" viewBox="0 0 505 154" aria-hidden="true">
    <defs>
      <linearGradient id="bottomGreen" x1="0" y1="0" x2="1" y2="0">
        <stop offset="0" stop-color="#a9d24c"/><stop offset="1" stop-color="#6fb32a"/>
      </linearGradient>
    </defs>
    <path d="M0 40 C150 30 260 60 310 58 L310 154 L0 154 Z" fill="url(#bottomGreen)"/>
    <path d="M0 52 C140 44 240 70 310 70 L310 154 L0 154 Z" fill="#d9ed9e" opacity=".55"/>
    <rect x="300" y="120" width="205" height="34" fill="url(#bottomGreen)"/>
  </svg>
  <div class="products-photo" role="img" aria-label="Photo of skincare products, nail polish bottles and manicured nails"></div>

  <div class="front-call">Call: +959 47208613</div>
  <div class="front-email">Email: contactus@velmora-unitedgroup.example</div>
  <div class="brands-note">We use well-known international brands in our spa including Veridelle, KRU, Varnet, Brisola Terrano and MORLU.</div>
</section>

</body>
</html>
```